依頼詳細
朝陽経済報を読むターゲットに対して
我々の広告を打ちます。

伝えたいことは「普通じゃダメなんです」
HPをご確認のうえ、ジムの印象などもご確認ください。
https://kx7fit.example/
記載項目
キャッチ:普通のおじさんでは、出世できない
リード:とはいえ、残念ながら日本は精神的に老化しやすい環境が揃っているそう。かっこよさは若い人の特権のように考えられ、『かっこよく歳を重ねる』という意識が少ない傾向にある。ぜひ、当ジムで「おじさん化対策」を実践して欲しい

黒地に白文字でのデザインを想定しております。
裏面に当社の情報をいれるため
引き付けて裏面をめくりたくなるようなA面のデザインを依頼させていただきます。
サイズ
A4
ページ数
片面
希望イメージ
シンプル 複雑
単色 カラフル
暗い 明るい
日常 高級
遊び心 厳粛
未来的 伝統的
女性的 男性的
希望する色
無彩色系
納品ファイル
• 高解像度JPG (.jpg)
• イラストレーター形式 (.ai)
補足説明
下記ロゴデータを画面どこかへ配置をお願いします。
我々で考えたデザイン案は下記になります。
これとは違うデザインをご提案いただきたいです。

「普通のおじさんでは出世できない」

提案いただいた中で、このキャッチを
「絶望」「恐怖」などで提案いただきましたが
「警告」として色味や主張をいただいた点が決め手となりました。
単色の差し色をも、新聞折り込みのチラシとしての相性も良く
弊社満場一致で可決となりました。

合計で60超の提案をいただきました。
皆様クリエイティブ溢れるアイディアをありがとうございました。

・キャッチコピーの受け取り方が想定と違う
・「おじさん」の中でもとらえられるイメージが違う

我々からの定義の中でも、
ご依頼方法を再考しないといけないなと考える学びもありました。
この度は皆様ご協力いただきありがとうございました!!

```html
<!DOCTYPE html>
<html lang="ja">
<head>
<meta charset="utf-8">
<title>普通のおじさんでは、出世できない — KX7フィットジム</title>
<link rel="stylesheet" href="https://fonts.googleapis.com/css2?family=Noto+Sans+JP:wght@400;500;900&family=Montserrat:wght@500&display=swap">
<style>
  :root {
    --ink: #ffffff;
    --ground: #000000;
    --glow: #8a8a8a;
    --lead: #e2e2e2;
    --sub: #bdbdbd;
  }
  html, body {
    margin: 0;
    padding: 0;
    width: 865px;
    height: 1200px;
    overflow: hidden;
    background: var(--ground);
  }
  .poster {
    position: relative;
    width: 865px;
    height: 1200px;
    background: var(--ground);
    overflow: hidden;
    font-family: "Noto Sans JP", sans-serif;
    color: var(--ink);
  }
  .burst {
    position: absolute;
    inset: 0;
  }
  .headline {
    position: absolute;
    top: 72px;
    right: 20px;
    margin: 0;
    writing-mode: vertical-rl;
    font-weight: 900;
    font-size: 122px;
    line-height: 186px;
    letter-spacing: 0;
    height: 490px;
  }
  .headline span {
    display: block;
  }
  .lead {
    position: absolute;
    top: 592px;
    left: 400px;
    width: 362px;
    margin: 0;
    font-size: 20px;
    line-height: 29px;
    font-weight: 500;
    color: var(--lead);
    letter-spacing: 0;
  }
  .brand {
    position: absolute;
    top: 872px;
    left: 0;
    width: 865px;
    display: flex;
    flex-direction: column;
    align-items: center;
  }
  .brand-row {
    display: flex;
    align-items: center;
    gap: 18px;
  }
  .brand-dot {
    width: 62px;
    height: 62px;
    border: 4px solid var(--ink);
    border-radius: 50%;
    box-sizing: border-box;
  }
  .brand-name {
    font-size: 42px;
    font-weight: 500;
    letter-spacing: 1px;
  }
  .brand-tag {
    margin-top: 6px;
    font-family: "Montserrat", sans-serif;
    font-size: 15px;
    letter-spacing: 1px;
    color: var(--sub);
  }
</style>
</head>
<body>
<main class="poster">
  <svg class="burst" viewBox="0 0 865 1200" role="img" aria-label="画面中央から放射状に広がる白いサンバースト模様">
    <defs>
      <radialGradient id="burstGlow" cx="420" cy="560" r="560" gradientUnits="userSpaceOnUse">
        <stop offset="0" stop-color="#8a8a8a"/>
        <stop offset="0.45" stop-color="#3a3a3a"/>
        <stop offset="1" stop-color="#000000"/>
      </radialGradient>
    </defs>
    <rect width="865" height="1200" fill="url(#burstGlow)"/>
  </svg>

  <h1 class="headline">
    <span>普通のお</span>
    <span>じさんで</span>
    <span>は、出世</span>
    <span>できない</span>
  </h1>

  <p class="lead">とはいえ、残念ながら日本は精神的に老化しやすい環境が揃っているそう。かっこよさは若い人の特権のように考えられ、『かっこよく歳を重ねる』という意識が少ない傾向にある。ぜひ、当ジムで「おじさん化対策」を実践して欲しい。</p>

  <div class="brand">
    <div class="brand-row">
      <div class="brand-dot"></div>
      <div class="brand-name">KX7フィットジム</div>
    </div>
    <div class="brand-tag">The fitness gym for grown-up men</div>
  </div>
</main>
</body>
</html>
```